Business Card Re-Design/Update

We'd like to update out business cards. I've included our current "Style guide" which has the colour scheme of the organisation in it. I've also included the branding files with logos etc in them.

I've also included a copy of one of our existing cards so that you can see how ugly/dated they look. I'd like a fresh modern corporate look.

Target Market(s)

These are for our clients, potential clients, industry contacts - like all business cards

Contact Information for Business Card

Name
Position
Company Address - Level 1, 47 Garnet Lane, Toowong Qld 4066
Direct Phone
mobile
Email
Website -www.korvalnet.com.au
Logo

Colors

Designer to choose colors to be used in the design.

Requirements
Must have
• Main Logo
• Cards will need to be editable to be able to personalize them for each new employee.
Nice to have
• The MapOUT, HandOVER, UpKEEP would be okay to have if they can be sensibly and professionally added to the look without detracting from the main imagery.
• Maybe they could go on the back of the card? will leave this to your creative discretion as to whether/where they fit.
Should not have
• Should not have decorative or script fonts

```html
<!DOCTYPE html>
<html lang="en">
<head>
<meta charset="utf-8">
<title>korvalnet business cards</title>
<link rel="stylesheet" href="https://fonts.googleapis.com/css2?family=Open+Sans:ital,wght@0,400;0,600;0,700;1,400&display=swap">
<style>
  :root{
    --page:#dcdcdc;
    --charcoal:#3c3d40;
    --red:#d7161e;
    --red-deep:#a9141b;
    --white:#f7f7f7;
    --ink:#3a3a3a;
    --light:#f2f2f2;
  }
  *{margin:0;padding:0;box-sizing:border-box}
  html,body{width:1200px;height:900px;overflow:hidden;background:var(--page);font-family:"Open Sans",Arial,sans-serif}
  .stage{position:relative;width:1200px;height:900px}
  .card{position:absolute;width:540px;height:330px;border-radius:22px;overflow:hidden;background:var(--white);box-shadow:0 8px 22px rgba(0,0,0,.18)}
  .card--contact{left:40px;top:285px}
  .card--brand{left:620px;top:285px}
  .card svg.art{position:absolute;inset:0}
  .contact-head{position:absolute;left:34px;top:30px;padding-left:14px;border-left:4px solid var(--red)}
  .contact-name{color:var(--light);font-size:25px;font-weight:400;line-height:1.1}
  .contact-role{color:var(--red);font-size:13px;font-style:italic;margin-top:2px}
  .contact-list{position:absolute;list-style:none;color:var(--light);font-size:12.5px}
  .contact-list li{display:flex;align-items:center;gap:7px;line-height:22px;white-space:nowrap}
  .contact-list svg{width:13px;height:13px;flex:none;fill:var(--red)}
  .contact-list--left{left:36px;top:104px}
  .contact-list--right{left:212px;top:104px}
  .contact-list--post{left:36px;top:158px}
  .address-line{padding-left:20px}
  .wordmark{display:flex;align-items:center;gap:10px;position:absolute;color:var(--ink);font-weight:400;letter-spacing:-.5px;white-space:nowrap}
  .wordmark-square{width:22px;height:22px;background:var(--red);flex:none}
  .card--contact .wordmark{right:30px;bottom:30px;font-size:36px}
  .card--brand .wordmark{left:272px;top:88px;font-size:40px}
  .card--brand .wordmark-square{width:26px;height:26px}
  .taglines{position:absolute;left:274px;top:160px;font-size:13px;font-weight:700;color:var(--ink);white-space:nowrap}
  .taglines .accent{color:var(--red)}
  .taglines .sep{color:var(--red);margin:0 7px;font-weight:400}
  .website{position:absolute;left:274px;top:232px;color:var(--red);font-size:14px;white-space:nowrap}
</style>
</head>
<body>
<main class="stage">

  <section class="card card--contact" aria-label="Business card, contact side">
    <svg class="art" viewBox="0 0 540 330" width="540" height="330" aria-hidden="true">
      <polygon points="0,0 470,0 385,40 352,205 0,205" fill="var(--charcoal)"/>
      <polygon points="385,40 470,0 540,0 540,8 412,70 372,205 352,205" fill="var(--red)"/>
      <polygon points="412,70 372,205 352,205 385,40" fill="var(--red-deep)"/>
      <polygon points="0,205 372,205 318,260 150,330 0,330" fill="var(--red)"/>
    </svg>

    <div class="contact-head">
      <p class="contact-name">Dana Whitlock</p>
      <p class="contact-role">Business Development Manager</p>
    </div>

    <ul class="contact-list contact-list--left">
      <li><svg viewBox="0 0 16 16"><path d="M4 0h8a1 1 0 0 1 1 1v14a1 1 0 0 1-1 1H4a1 1 0 0 1-1-1V1a1 1 0 0 1 1-1zm1 2v10h6V2z"/></svg>+61 (0)412 560 384</li>
      <li><svg viewBox="0 0 16 16"><path d="M1 5c0-2 3-3 7-3s7 1 7 3v1h-4V5H5v1H1zm2 2h10l2 8H1z"/></svg>+61 (0)7 3300 1420</li>
    </ul>
    <ul class="contact-list contact-list--right">
      <li><svg viewBox="0 0 16 16"><path d="M1 5c0-2 3-3 7-3s7 1 7 3v1h-4V5H5v1H1zm2 2h10l2 8H1z"/></svg>+61 (0)7 3300 1427</li>
      <li><svg viewBox="0 0 16 16"><path d="M4 0h6v5H4zM2 6h12a1 1 0 0 1 1 1v8H1V7a1 1 0 0 1 1-1zm2 3v2h8V9z"/></svg>+61 (0)7 3300 1429</li>
    </ul>
    <ul class="contact-list contact-list--post">
      <li><svg viewBox="0 0 16 16"><path d="M0 3h16v10H0zm1 1v1l7 4 7-4V4z"/></svg>dwhitlock@korvalnet.com.au</li>
      <li><svg viewBox="0 0 16 16"><path d="M8 0a5 5 0 0 1 5 5c0 4-5 11-5 11S3 9 3 5a5 5 0 0 1 5-5zm0 3a2 2 0 1 0 0 4 2 2 0 0 0 0-4z"/></svg>Level 1, 47 Garnet Lane</li>
      <li class="address-line">Toowong Qld 4066</li>
    </ul>

    <div class="wordmark"><span class="wordmark-square"></span>korvalnet</div>
  </section>

  <section class="card card--brand" aria-label="Business card, brand side">
    <svg class="art" viewBox="0 0 540 330" width="540" height="330" aria-hidden="true">
      <polygon points="0,0 330,0 280,40 245,110 225,200 0,200" fill="var(--charcoal)"/>
      <polygon points="280,40 330,0 372,0 302,52 262,112 238,200 225,200 245,110" fill="var(--red)"/>
      <polygon points="302,52 262,112 238,200 225,200 245,110 280,40" fill="var(--red-deep)"/>
      <polygon points="0,200 238,200 190,262 100,330 0,330" fill="var(--red)"/>
    </svg>

    <div class="wordmark"><span class="wordmark-square"></span>korvalnet</div>

    <p class="taglines">Map<span class="accent">OUT</span><span class="sep">|</span>Hand<span class="accent">OVER</span><span class="sep">|</span>Up<span class="accent">KEEP</span></p>
    <p class="website">www.korvalnet.com.au</p>
  </section>

</main>
</body>
</html>
```